Upmarket cover for top management book, ideally unlike most common cover pages

This book is about both good management and mismanagement and introduces novel concepts such as the inverse exponential law in strategy, No doubt that these concepts will be criticized by some management scholars. However, students, a few other colleagues and key top managers find the new ideas useful and eye-opening.
The cover must help communicate a deeper vision of management as an expression of life creation and a sort of "divine" energy.

Practical details:
Print and ebook cover page plus elements of the cover for each of the three main book sections.
Title; The Harbor
Subtitle: Field methods and the quiet ripple rule
Author: Teodor M. Vasquel
Publisher: Brightwell Page Press
Width x height: 13,97 x 21,59 cm (without bleed)
Spine: 14-15 cm according to paper color

Target Market(s)

Mostly managers who did not have the opportunity of attending postgraduate management studies such as the MBA

Industry/Entity Type

Mostly high technology

Font styles to use
Serif
Sans Serif
Other font styles liked:
• Arial nova, Arial light

Requirements
Must have
• Preferably cover and back cover on white background, but any good proposals would do.
Nice to have
• An image of bright and reassuring, albeit potentially unlimited, strength. Ideally the cover design should show that good management is good for the COMMON GOOD of society
Should not have
• Please do not show images of people and no proposals reminiscent of other management and strategy book covers

```html
<!DOCTYPE html>
<html lang="en">
<head>
<meta charset="utf-8">
<title>The Harbor — Book Cover</title>
<link rel="stylesheet" href="https://fonts.googleapis.com/css2?family=Cinzel:wght@400;500;600;700&display=swap">
<style>
  :root {
    --backdrop: #d2d2d2;
    --cover-paper: #f5f5f5;
    --title-red: #e11b25;
    --subtitle-ink: #2b2b2b;
    --dial-white: #ffffff;
    --dial-light: #ececec;
    --dial-mid: #c9c9c9;
    --dial-dark: #8c8c8c;
    --needle-red: #e11b25;
    --needle-orange: #f08a1c;
  }
  * { margin: 0; padding: 0; box-sizing: border-box; }
  html, body {
    width: 1162px;
    height: 1200px;
    overflow: hidden;
    background: var(--backdrop);
  }
  .book-cover {
    position: absolute;
    left: 247px;
    top: 83px;
    width: 667px;
    height: 1033px;
    background: var(--cover-paper);
    font-family: "Cinzel", "Times New Roman", serif;
  }
  .cover-title {
    position: absolute;
    left: 0;
    top: 62px;
    width: 100%;
    text-align: center;
    color: var(--title-red);
    font-weight: 600;
    font-size: 130px;
    line-height: 104px;
    text-transform: uppercase;
    letter-spacing: -1px;
  }
  .cover-subtitle {
    position: absolute;
    left: 0;
    top: 306px;
    width: 100%;
    text-align: center;
    color: var(--subtitle-ink);
    font-weight: 700;
    font-size: 33px;
    line-height: 32px;
    letter-spacing: 0.5px;
  }
  .cover-emblem {
    position: absolute;
    left: 118px;
    top: 431px;
    width: 436px;
    height: 436px;
  }
  .cover-author {
    position: absolute;
    left: 0;
    top: 922px;
    width: 100%;
    text-align: center;
    color: var(--title-red);
    font-weight: 600;
    font-size: 46px;
    line-height: 50px;
    letter-spacing: 0.5px;
  }
</style>
</head>
<body>
  <main class="book-cover">
    <h1 class="cover-title">The<br>Harbor</h1>
    <p class="cover-subtitle">Field methods and the<br>quiet ripple rule</p>
    <svg class="cover-emblem" viewBox="0 0 436 436" role="img" aria-label="Illustration of a white compass rose with a red and orange needle pointing north-north-east, symbolising direction and steady strength">
      <defs>
        <radialGradient id="dial-tone" cx="50%" cy="50%" r="50%">
          <stop offset="0%" stop-color="var(--dial-mid)"/>
          <stop offset="30%" stop-color="var(--dial-light)"/>
          <stop offset="62%" stop-color="var(--dial-white)"/>
          <stop offset="82%" stop-color="var(--dial-light)"/>
          <stop offset="100%" stop-color="var(--dial-white)"/>
        </radialGradient>
      </defs>
      <circle cx="218" cy="218" r="215" fill="url(#dial-tone)" stroke="var(--dial-dark)" stroke-width="3"/>
    </svg>
    <p class="cover-author">Teodor M. Vasquel</p>
  </main>
</body>
</html>
```